4 x Designs Required

Hi There,
I require 4 x different designs to be made for 4 new brands of mine however they can be quite interchangeable. HR Plinkr and Marketing Plinkr can be similar just with a difference in colour. The same goes for the Bulletin brands. This means there are ultimately two designs that need perfecting.

There must be a click here CTA on the banner somewhere. :-)

I require the banners in 728x90 format and 960x90 please.

Please use strap lines on the banners such as:
Essential Whitepapers for HR Professionals
Essential Whitepapers for Marketing Professionals
Your No.1 Whitepaper Resource

The brand names:
HR Plinkr
Marketing Plinkr
HR Dispatchly
Marketing Dispatchly

Examples attached.

```html
<!DOCTYPE html>
<html lang="en">
<head>
<meta charset="utf-8">
<title>Whitepaper Banner Set</title>
<link rel="stylesheet" href="https://fonts.googleapis.com/css2?family=Poppins:wght@700;800;900&display=swap">
<style>
  :root {
    --canvas: #7f95d3;
    --navy-deep: #0d1f3f;
    --navy-mid: #17325e;
    --teal-deep: #03182a;
    --teal-mid: #0b3550;
    --cocoa: #2a1f21;
    --cocoa-light: #2f2427;
    --midnight: #021428;
    --midnight-mid: #04203a;
    --white: #ffffff;
    --cyan: #0fd8ec;
    --cyan-ink: #0b2547;
    --green: #22b14c;
    --emerald: #22ad6e;
    --tan: #c49a6c;
    --tan-ink: #2a1f21;
  }
  * { margin: 0; padding: 0; box-sizing: border-box; }
  html, body {
    width: 1200px; height: 982px; overflow: hidden;
    background: var(--canvas);
    font-family: "Poppins", Arial, sans-serif;
  }
  .banner-set { position: relative; width: 1200px; height: 982px; }
  .banner {
    position: absolute; left: 71px; width: 1058px; height: 98px;
    overflow: hidden; color: var(--white); text-transform: uppercase;
  }
  .banner > * { position: absolute; top: 50%; transform: translateY(-50%); white-space: nowrap; }
  .backdrop { inset: 0; top: 0; transform: none; }

  /* Plinkr – HR */
  .banner--hr-plinkr .backdrop { background: linear-gradient(100deg, var(--navy-deep) 0%, var(--navy-mid) 55%, var(--navy-deep) 100%); }
  .banner--hr-plinkr .brand { left: 24px; font-size: 40px; font-weight: 900; letter-spacing: -0.5px; }
  .banner--hr-plinkr .strapline { left: 270px; font-size: 22px; font-weight: 800; letter-spacing: -0.3px; }
  .banner--hr-plinkr .accent { color: var(--cyan); }
  .banner--hr-plinkr .cta {
    left: 906px; width: 144px; height: 39px; border-radius: 20px;
    background: var(--cyan); color: var(--cyan-ink);
    font-size: 17px; font-weight: 700; display: flex; align-items: center; justify-content: center;
    box-shadow: 0 2px 0 rgba(0,0,0,0.25);
  }

  /* Dispatchly – HR */
  .banner--hr-dispatchly .backdrop { background: radial-gradient(ellipse at 85% 30%, var(--teal-mid) 0%, var(--teal-deep) 65%); }
  .banner--hr-dispatchly .brand { left: 22px; font-size: 26px; font-weight: 800; }
  .banner--hr-dispatchly .strapline { left: 252px; font-size: 32px; font-weight: 800; letter-spacing: -0.3px; }
  .banner--hr-dispatchly .accent { color: var(--green); }
  .banner--hr-dispatchly .cta {
    left: 897px; width: 144px; height: 39px; border-radius: 20px;
    background: var(--green); color: var(--white);
    font-size: 17px; font-weight: 700; display: flex; align-items: center; justify-content: center;
    box-shadow: 0 2px 0 rgba(0,0,0,0.3);
  }

  /* Plinkr – Marketing */
  .banner--mkt-plinkr .backdrop { background: linear-gradient(90deg, var(--cocoa) 0%, var(--cocoa-light) 50%, var(--cocoa) 100%); }
  .banner--mkt-plinkr .brand { left: 20px; font-size: 22px; font-weight: 800; color: var(--tan); }
  .banner--mkt-plinkr .strapline { left: 275px; font-size: 20px; font-weight: 800; letter-spacing: -0.3px; }
  .banner--mkt-plinkr .accent { color: var(--tan); }
  .banner--mkt-plinkr .cta {
    left: 948px; width: 132px; height: 132px; border-radius: 50%;
    background: var(--tan); color: var(--tan-ink);
    font-size: 26px; font-weight: 900; line-height: 1; padding-left: 10px;
    display: flex; flex-direction: column; justify-content: center; align-items: flex-start;
  }
  .banner--mkt-plinkr .cta span { display: block; }
  .banner--mkt-plinkr .cta span + span { margin-top: 2px; padding-left: 1px; }

  /* Dispatchly – Marketing */
  .banner--mkt-dispatchly .backdrop { background: linear-gradient(90deg, var(--midnight) 0%, var(--midnight-mid) 60%, var(--midnight) 100%); }
  .banner--mkt-dispatchly .brand { left: 22px; font-size: 22px; font-weight: 800; color: var(--emerald); }
  .banner--mkt-dispatchly .strapline { left: 348px; font-size: 26px; font-weight: 800; letter-spacing: -0.3px; }
  .banner--mkt-dispatchly .accent { color: var(--emerald); }
  .banner--mkt-dispatchly .cta {
    left: 894px; width: 144px; height: 39px; border-radius: 20px;
    background: var(--emerald); color: var(--white);
    font-size: 17px; font-weight: 700; display: flex; align-items: center; justify-content: center;
    box-shadow: 0 2px 0 rgba(0,0,0,0.3);
  }
</style>
</head>
<body>
<main class="banner-set">

  <section class="banner banner--hr-plinkr" style="top:26px">
    <div class="backdrop" role="img" aria-label="Blue network line pattern background"></div>
    <div class="brand">HR Plinkr</div>
    <p class="strapline"><span class="accent">Essential</span> Whitepapers <span class="accent">for HR Professionals</span></p>
    <a class="cta">Click Here</a>
  </section>

  <section class="banner banner--hr-plinkr" style="top:145px">
    <div class="backdrop" role="img" aria-label="Blue network line pattern background"></div>
    <div class="brand">HR Plinkr</div>
    <p class="strapline">Essential Whitepapers for HR Professionals</p>
    <a class="cta">Click Here</a>
  </section>

  <section class="banner banner--hr-dispatchly" style="top:264px">
    <div class="backdrop" role="img" aria-label="Dark teal connected-dots network background"></div>
    <div class="brand">HR Dispatchly</div>
    <p class="strapline"><span class="accent">Your No.1</span> Whitepaper <span class="accent">Resource</span></p>
    <a class="cta">Click Here</a>
  </section>

  <section class="banner banner--hr-dispatchly" style="top:383px">
    <div class="backdrop" role="img" aria-label="Dark teal connected-dots network background"></div>
    <div class="brand">HR Dispatchly</div>
    <p class="strapline">Your No.1 Whitepaper Resource</p>
    <a class="cta">Click Here</a>
  </section>

  <section class="banner banner--mkt-plinkr" style="top:502px">
    <div class="backdrop" role="img" aria-label="Dark brown background with faint dot pattern"></div>
    <div class="brand">Marketing Plinkr</div>
    <p class="strapline"><span class="accent">Essential</span> Whitepapers <span class="accent">for Marketing Professionals</span></p>
    <a class="cta"><span>Click</span><span>Here</span></a>
  </section>

  <section class="banner banner--mkt-plinkr" style="top:621px">
    <div class="backdrop" role="img" aria-label="Dark brown background with faint dot pattern"></div>
    <div class="brand">Marketing Plinkr</div>
    <p class="strapline">Essential Whitepapers for Marketing Professionals</p>
    <a class="cta"><span>Click</span><span>Here</span></a>
  </section>

  <section class="banner banner--mkt-dispatchly" style="top:740px">
    <div class="backdrop"></div>
    <div class="brand">Marketing Dispatchly</div>
    <p class="strapline"><span class="accent">Your No.1</span> Whitepaper <span class="accent">Resource</span></p>
    <a class="cta">Click Here</a>
  </section>

  <section class="banner banner--mkt-dispatchly" style="top:859px">
    <div class="backdrop"></div>
    <div class="brand">Marketing Dispatchly</div>
    <p class="strapline">Your No.1 Whitepaper Resource</p>
    <a class="cta">Click Here</a>
  </section>

</main>
</body>
</html>
```